bluefinwardco.com website design

We're looking for a website design for Bluefinwardco.com .
Bluefinward is a manufacturer of high visibility traffic safety equipment and gear.. Our initial site will be a product catalog site featuring traffic cones . We will eventually expand to include traffic barriers, mesh signs, safety clothing and more. Our logo and product pictures can be found at bluefinwardco.com .
Updates

Need extra days to review

Target Market(s)

We service a wide range of customers with our focus markets being construction, manufacturing and municipalities.

Industry/Entity Type

Safety Products

Number of Pages Required

1 page

Font styles to use
Sans Serif

Requirements
Must have
• company logo w/compatible color scheme

```html
<!DOCTYPE html>
<html lang="en">
<head>
<meta charset="utf-8">
<title>Bluefinward Safety Products</title>
<link href="https://fonts.googleapis.com/css2?family=Poppins:wght@400;500;600;700;800&display=swap" rel="stylesheet">
<style>
:root{
  --orange:#e8842a;
  --orange-deep:#e05a1c;
  --amber:#f5b73c;
  --ink:#1d1d1d;
  --text:#555;
  --line:#e7e7e7;
  --black:#0b0b0b;
  --white:#fff;
}
*{margin:0;padding:0;box-sizing:border-box}
html,body{width:1200px;height:3187px;overflow:hidden;background:var(--white)}
body{position:relative;font-family:'Poppins',sans-serif;color:var(--ink)}
.abs{position:absolute}
.btn{position:absolute;display:flex;align-items:center;justify-content:center;border-radius:30px;
  background:linear-gradient(90deg,var(--amber),var(--orange));color:var(--white);font-weight:700;font-size:16px;text-transform:uppercase}
/* header */
.topline{left:0;top:0;width:1200px;height:3px;background:var(--orange)}
.brand{left:111px;top:26px;display:flex;align-items:center;gap:8px}
.brand-dot{width:30px;height:30px;border-radius:50%;background:var(--orange)}
.brand-name{font-size:24px;font-weight:600;color:var(--orange)}
.nav a{position:absolute;top:33px;font-size:14px;font-weight:500;color:var(--ink);text-decoration:none}
.quote{left:951px;top:21px;width:138px;height:41px;font-size:15px}
/* hero */
.hero{left:0;top:84px;width:1200px;height:515px;
  background:radial-gradient(ellipse at 78% 50%,#e8602a 0%,#d7552a 12%,rgba(90,85,70,.2) 30%),linear-gradient(180deg,#3f5a35 0%,#5f6b52 30%,#6c6c66 55%,#4a4a48 100%)}
.hero-title{left:111px;top:170px;font-size:59px;line-height:60px;font-weight:800;color:var(--white)}
.hero-copy{left:113px;top:366px;width:462px;font-size:15px;line-height:24px;color:var(--white)}
.shop{left:113px;top:463px;width:136px;height:40px}
.dots{left:576px;top:553px;display:flex;gap:8px;align-items:center}
.dots span{width:6px;height:6px;border-radius:50%;background:var(--white)}
.dots .on{width:16px;height:16px;border:2px solid var(--white);background:transparent}
/* section titles */
.sec-title{left:0;width:1200px;text-align:center;font-size:42px;font-weight:700;text-transform:uppercase}
/* filters */
.filter{position:absolute;top:731px;height:44px;border:2px solid var(--amber);border-radius:24px;display:flex;align-items:center;justify-content:center;font-size:18px;color:#666}
.filter.active{border:none;background:linear-gradient(90deg,var(--amber),var(--orange));color:var(--white);font-weight:700;font-size:16px}
/* products */
.card{position:absolute;width:234px;height:219px;border:1px solid var(--line);background:var(--white)}
.card .pic{position:absolute;left:6px;top:6px;right:6px;bottom:6px}
.tag{position:absolute;top:7px;right:7px;background:var(--orange);color:var(--white);font-size:9px;padding:3px 7px}
.pname{position:absolute;width:234px;text-align:center;font-size:12px;color:#444}
.stars{position:absolute;width:234px;text-align:center;font-size:10px;color:var(--orange-deep);letter-spacing:1px}
.more{left:532px;top:1458px;width:136px;height:41px}
/* testimonials */
.band{left:0;top:1578px;width:1200px;height:474px;background:linear-gradient(180deg,#e8913f,#e2893a)}
.band-sub{left:230px;top:1698px;width:740px;text-align:center;font-size:13px;line-height:21px;color:var(--white)}
.review{position:absolute;top:1785px;width:428px;height:162px;background:var(--white);border-radius:42px}
.review p{position:absolute;left:74px;top:30px;width:320px;font-size:12.5px;line-height:22px;color:#666}
.review h4{position:absolute;left:74px;top:110px;font-size:15px;font-weight:600;color:var(--orange)}
.avatar{position:absolute;top:1824px;width:86px;height:86px;border-radius:50%;border:3px solid var(--white);background:linear-gradient(160deg,#c9b39a,#8f7a66)}
.qmark{position:absolute;right:34px;top:104px}
/* about */
.frame{left:113px;top:2150px;width:194px;height:194px;border:2px solid var(--amber)}
.about-pic{left:166px;top:2211px;width:440px;height:350px;background:linear-gradient(135deg,#3f7bd0 0%,#4a8ee0 45%,#e67a2a 70%,#6f6f6f 100%);box-shadow:0 6px 18px rgba(0,0,0,.2)}
.about-title{left:695px;top:2163px;font-size:42px;font-weight:700}
.about-copy{left:680px;top:2228px;width:405px;font-size:15.5px;line-height:24px;color:#666}
.read{left:680px;top:2495px;width:136px;height:40px}
/* footer */
.foot-bg{left:0;top:0}
.news{left:172px;top:2700px;width:856px;height:170px;background:var(--white);border-radius:85px}
.news h3{position:absolute;left:0;top:26px;width:856px;text-align:center;font-size:29px;font-weight:700;text-transform:uppercase}
.news p{position:absolute;left:150px;top:70px;width:556px;text-align:center;font-size:10.5px;line-height:17px;color:#555}
.field{position:absolute;left:190px;top:117px;width:476px;height:34px;border:2px solid var(--amber);border-radius:20px;font-size:12px;color:#777;display:flex;align-items:center;padding-left:24px}
.sub{left:631px;top:2817px;width:207px;height:34px;font-size:14px}
.col{position:absolute;top:2933px;color:var(--white)}
.col h5{font-size:26px;font-weight:700;text-transform:uppercase;margin-bottom:14px}
.col li{list-style:none;font-size:17.5px;line-height:29.3px}
.copy{left:0;top:3150px;width:1200px;text-align:center;font-size:12px;color:var(--white)}
</style>
</head>
<body>

<div class="abs topline"></div>
<div class="abs brand"><span class="brand-dot"></span><span class="brand-name">Bluefinward</span></div>
<nav class="nav">
  <a style="left:393px" href="#">HOME</a>
  <a style="left:481px" href="#">ABOUT US</a>
  <a style="left:599px" href="#">PRODUCTS</a>
  <a style="left:722px" href="#">REVIEWS</a>
  <a style="left:830px" href="#">CONTACT US</a>
</nav>
<div class="btn quote">Get a Quote</div>

<section class="abs hero" role="img" aria-label="Traffic cone standing on an asphalt road with blurred trees behind"></section>
<h1 class="abs hero-title">WELCOME TO<br>BLUEFINWARD<br>SAFETY PRODUCTS</h1>
<p class="abs hero-copy">It is a long established fact that a reader will be distracted by the readable content of a page when looking at its layout. The point of using</p>
<div class="btn shop">Shop Now</div>
<div class="abs dots"><span></span><span class="on"></span><span></span></div>

<h2 class="abs sec-title" style="top:655px">Shop Our Products</h2>
<div class="filter active" style="left:150px;width:136px">ALL</div>
<div class="filter" style="left:304px;width:173px">Traffic Cones</div>
<div class="filter" style="left:496px;width:173px">Traffic Barriers</div>
<div class="filter" style="left:688px;width:173px">Mesh Signs</div>
<div class="filter" style="left:880px;width:173px">Safety Clothing</div>

<div class="card" style="left:111px;top:823px"><div class="pic" role="img" aria-label="Hard hat with orange cones" style="background:linear-gradient(135deg,#fff 20%,#f3b23a 45%,#e8622a 70%,#fff 95%)"></div><span class="tag">2 Reflective Collars</span></div>
<div class="card" style="left:359px;top:823px"><div class="pic" role="img" aria-label="Orange traffic barrel with warning light" style="background:linear-gradient(180deg,#6b7a52 0%,#e9782e 45%,#e35f22 80%,#cfcfcf 100%)"></div></div>
<div class="card" style="left:607px;top:823px"><div class="pic" role="img" aria-label="Utility work ahead roadside sign" style="background:linear-gradient(180deg,#6d6b58 0%,#e06a25 45%,#5b5b5b 100%)"></div><span class="tag">New Arrivals</span></div>
<div class="card" style="left:855px;top:823px"><div class="pic" role="img" aria-label="Road closed barricade" style="background:linear-gradient(180deg,#9fb4c9 0%,#d4c9b5 40%,#c9a23a 60%,#9c9c9c 100%)"></div></div>
<div class="pname" style="left:111px;top:1063px">Orange Cone</div><div class="stars" style="left:111px;top:1088px">★★★★☆</div>
<div class="pname" style="left:359px;top:1063px">Traffic Barriers</div><div class="stars" style="left:359px;top:1088px">★★★★☆</div>
<div class="pname" style="left:607px;top:1063px">Mesh Signs</div><div class="stars" style="left:607px;top:1088px">★★★★☆</div>
<div class="pname" style="left:855px;top:1063px">Traffic Barriers</div><div class="stars" style="left:855px;top:1088px">★★★★☆</div>

<div class="card" style="left:111px;top:1129px"><div class="pic" role="img" aria-label="Rack of high visibility vests" style="background:linear-gradient(90deg,#c7e23a,#e8722a,#d5e83a,#3f7a4a)"></div></div>
<div class="card" style="left:359px;top:1129px"><div class="pic" role="img" aria-label="Lime green traffic cone" style="background:radial-gradient(ellipse at 50% 55%,#b4f02a 0%,#c9f35e 25%,#fff 55%)"></div><span class="tag">2 Reflective Collars</span></div>
<div class="card" style="left:607px;top:1129px"><div class="pic" role="img" aria-label="Worker in high visibility jacket" style="background:linear-gradient(180deg,#7b8470 0%,#bde040 45%,#e4582a 70%,#5a5a5a 100%)"></div><span class="tag">New Arrivals</span></div>
<div class="card" style="left:855px;top:1129px"><div class="pic" role="img" aria-label="Collection of road signs" style="background:linear-gradient(135deg,#2f5fb0,#e83a2a 35%,#f3d23a 60%,#2d8a3a 85%)"></div></div>
<div class="pname" style="left:111px;top:1370px">Safety Clothing</div><div class="stars" style="left:111px;top:1395px">★★★★☆</div>
<div class="pname" style="left:359px;top:1370px">Lime Cone</div><div class="stars" style="left:359px;top:1395px">★★★★☆</div>
<div class="pname" style="left:607px;top:1370px">Safety Clothing</div><div class="stars" style="left:607px;top:1395px">★★★★☆</div>
<div class="pname" style="left:855px;top:1370px">Mesh Signs</div><div class="stars" style="left:855px;top:1395px">★★★★☆</div>

<div class="btn more">View More</div>

<section class="abs band"></section>
<h2 class="abs sec-title" style="top:1632px;color:var(--white)">Our Happy Customers</h2>
<p class="abs band-sub">It is a long established fact that a reader will be distracted by the readable content of a page when looking at its layout. The point of using Lorem Ipsum is that it has a more-or-less normal</p>

<div class="review" style="left:155px">
  <p>It is a long established fact that a reader will be distracted by the readable content of a page when looking at its layout.</p>
  <h4>Daniel Reyes</h4>
  <svg class="qmark" width="48" height="40" viewBox="0 0 48 40"><path d="M0 40V22C0 9 7 2 20 0v8c-7 2-10 6-10 12h10v20zM26 40V22C26 9 33 2 46 0v8c-7 2-10 6-10 12h10v20z" fill="#cfcfcf"/></svg>
</div>
<div class="avatar" style="left:112px" role="img" aria-label="Customer portrait"></div>
<div class="review" style="left:659px">
  <p>It is a long established fact that a reader will be distracted by the readable content of a page when looking at its layout.</p>
  <h4>Priya Nair</h4>
  <svg class="qmark" width="48" height="40" viewBox="0 0 48 40"><path d="M0 40V22C0 9 7 2 20 0v8c-7 2-10 6-10 12h10v20zM26 40V22C26 9 33 2 46 0v8c-7 2-10 6-10 12h10v20z" fill="#cfcfcf"/></svg>
</div>
<div class="avatar" style="left:616px;background:linear-gradient(160deg,#6fb8e8,#e8722a)" role="img" aria-label="Customer portrait"></div>
<svg class="abs" style="left:571px;top:1972px" width="62" height="14" viewBox="0 0 62 14"><path d="M20 7H2M8 1 2 7l6 6" stroke="#f6c9a0" stroke-width="1.5" fill="none"/><path d="M30 7h30M54 1l6 6-6 6" stroke="#fff" stroke-width="1.5" fill="none"/></svg>

<div class="abs frame"></div>
<div class="abs about-pic" role="img" aria-label="Road worker painting lane markings on a blue surface"></div>
<h2 class="abs about-title">ABOUT US</h2>
<p class="abs about-copy">It is a long established fact that a reader will be distracted by the readable content of a page when looking at its layout. The point of using Lorem Ipsum is that it has a more-or-less normal distribution of letters, as opposed to using 'Content here, content here', making it look like readable English. Many desktop publishing packages and web page editors now use Lorem Ipsum as their default model text, and a search for 'lorem ipsum' will uncover many web sites still in their infancy.</p>
<div class="btn read">Read More</div>

<svg class="abs foot-bg" width="1200" height="3187" viewBox="0 0 1200 3187"><path d="M0 2580C80 2760 250 2840 470 2840C720 2840 900 2700 1200 2680V3187H0Z" fill="#0b0b0b"/></svg>

<div class="abs news">
  <h3>Sign Up to Our Newsletter</h3>
  <p>The standard chunk of Lorem Ipsum used since the 1500s is reproduced below for those interested. Sections 1.10.32 and 1.10.33 from "de Finibus Bonorum et Malorum"</p>
  <div class="field">Email Address</div>
</div>
<div class="btn sub">Subscribe</div>

<div class="col" style="left:155px"><h5>Quick Links</h5><ul><li>Home</li><li>About Us</li><li>Reviews</li><li>Contact Us</li></ul></div>
<div class="col" style="left:418px"><h5>Products</h5><ul><li>Traffic Cones</li><li>Traffic Barriers</li><li>Mesh Signs</li><li>Safety Clothing</li></ul></div>
<div class="col" style="left:661px"><h5>Help Links</h5><ul><li>Help</li><li>Privacy Policy</li><li>Terms Of Use</li><li>Return</li></ul></div>
<div class="col" style="left:899px"><h5>Follow Us</h5><ul><li>Crowdhall</li><li>Snapwell</li><li>Workgrid</li><li>Chirpline</li></ul></div>
<p class="abs copy">© Copyright 2023 Bluefinward Safety Products | All Rights Reserved</p>

</body>
</html>
```